Marlow Tide Resort Post Card

I want to do a Just Listed and a Just Sold Postcard for the condo community Marlow Tide Resort. It will be a glossy color front and back postcard. I am attaching some images and examples of what I like.

On the sample just sold I like the big "just sold" and I like the design on the side that fades into another picture.

I like to the exterior picture entrance that then maybe fades to the pool and faded pool pic on rear

On the rear sample there is too much dead space on the addressee side. I would like to put my brenda kettle logo and contact info all across the bottom.

I like the faded picture as the background for the entire rear of the card.

Maybe use the reverse photos for just Sold-- Main pool pic and faded exterior pic.

I also included tennis court, basketball court and interior shot that you may or may not use. I don't want to over crowd it.

I would like to emphasize my logo and somewhat downplay the R and P logo. my contact info is brendakettle@brendakettlehomes.example and my phone is 555-203-7746
I am open to suggestions

```html
<!DOCTYPE html>
<html lang="en">
<head>
<meta charset="utf-8">
<title>Marlow Tide Resort – Just Sold Postcard</title>
<link rel="stylesheet" href="https://fonts.googleapis.com/css2?family=Archivo+Black&family=Lato:wght@400;700;900&family=Tinos:wght@700&display=swap">
<style>
  :root {
    --backdrop: #3b3b3b;
    --yellow: #f7dc2a;
    --yellow-light: #fbee7a;
    --orange: #f28a1c;
    --orange-text: #e98a2b;
    --blue: #3d5a9e;
    --blue-text: #2a4a9a;
    --ink: #222222;
    --white: #ffffff;
    --faded: #e4e6e4;
  }
  * { box-sizing: border-box; margin: 0; padding: 0; }
  html, body { width: 842px; height: 1200px; overflow: hidden; }
  body { background: var(--backdrop); position: relative; font-family: "Lato", sans-serif; }

  .card { position: absolute; overflow: hidden; background: var(--white); }
  .card-front { left: 80px; top: 50px; width: 688px; height: 532px; }
  .card-back { left: 80px; top: 612px; width: 690px; height: 536px; }
  .card svg.shapes { position: absolute; left: 0; top: 0; }

  .resort-title {
    position: absolute; left: 0; width: 550px; top: 18px; text-align: center;
    font-family: "Tinos", serif; font-weight: 700; font-size: 27px; color: var(--orange-text);
  }
  .sun-art {
    position: absolute; left: 240px; top: 48px; width: 68px; height: 68px; border-radius: 50%;
    background: radial-gradient(circle, #f2b21c 0%, #f5c62a 55%, rgba(247,220,42,0) 72%);
  }
  .headline {
    position: absolute; left: 24px; top: 228px;
    font-family: "Archivo Black", sans-serif; font-size: 50px; letter-spacing: 1px; color: var(--white);
    text-shadow: 2px 2px 4px rgba(0,0,0,.55);
  }

  .agent-mark { position: absolute; text-align: center; }
  .agent-mark .agent-name { font-family: "Lato", sans-serif; font-weight: 400; letter-spacing: 2px; }
  .agent-mark .agent-title { font-weight: 700; letter-spacing: 2px; }
  .card-front .agent-mark { left: 36px; top: 452px; }
  .card-front .agent-name { font-size: 28px; color: var(--blue-text); }
  .card-front .agent-title { font-size: 13px; color: var(--orange-text); margin-top: 2px; }

  .brokerage-mark { position: absolute; display: flex; align-items: center; gap: 8px; }
  .brokerage-mark .mark-square { width: 22px; height: 22px; background: #8ea3c8; }
  .brokerage-mark .brokerage-name { font-size: 20px; font-weight: 700; color: var(--ink); }
  .card-front .brokerage-mark { left: 552px; top: 466px; }
  .card-back .brokerage-mark { left: 18px; top: 34px; }

  .return-address { position: absolute; left: 154px; top: 26px; color: var(--blue-text); font-style: normal; }
  .return-address .name { font-size: 19px; }
  .return-address .line { font-size: 13px; line-height: 17px; }

  .sale-note { position: absolute; left: 23px; top: 138px; width: 330px; font-size: 19px; color: var(--ink); line-height: 28px; }
  .sale-note .rule { height: 1px; background: var(--ink); margin-bottom: 8px; }
  .blank { display: inline-block; border-bottom: 1px solid var(--ink); height: 18px; vertical-align: baseline; }
  .call-to-action {
    position: absolute; left: 26px; top: 232px; width: 330px;
    font-size: 19.5px; font-weight: 700; line-height: 30px; color: var(--blue-text);
  }
  .stamp-box { position: absolute; left: 637px; top: 89px; width: 27px; height: 75px; background: var(--white); border: 1px solid #333; }

  .contact-strip { position: absolute; left: 0; right: 0; top: 388px; text-align: center; }
  .card-back .agent-mark { position: static; margin: 0 0 6px 30px; }
  .card-back .agent-name { font-size: 26px; color: var(--ink); }
  .card-back .agent-title { font-size: 13px; color: var(--ink); }
  .contact-line { font-size: 25px; color: var(--orange-text); line-height: 34px; }
</style>
</head>
<body>

<section class="card card-front">
  <svg class="shapes" width="688" height="532" viewBox="0 0 688 532">
    <defs>
      <linearGradient id="topWash" x1="0" y1="0" x2="1" y2="0">
        <stop offset="0" stop-color="#fbe85a"/>
        <stop offset="1" stop-color="#f7d92a"/>
      </linearGradient>
      <linearGradient id="entranceTones" x1="0" y1="0" x2="0" y2="1">
        <stop offset="0" stop-color="#7fb4e6"/>
        <stop offset=".5" stop-color="#c9d6de"/>
        <stop offset="1" stop-color="#5f8f4a"/>
      </linearGradient>
      <linearGradient id="poolTones" x1="0" y1="0" x2="0" y2="1">
        <stop offset="0" stop-color="#7f9a6a"/>
        <stop offset=".45" stop-color="#d8d6c8"/>
        <stop offset=".7" stop-color="#3fb0b8"/>
        <stop offset="1" stop-color="#3e6b38"/>
      </linearGradient>
    </defs>
    <rect width="688" height="200" fill="url(#topWash)"/>
    <g role="img" aria-label="Photo of the resort entrance with palm trees and condo buildings">
      <path d="M0,85 C130,60 260,175 430,150 L480,425 C330,380 150,330 0,348 Z" fill="url(#entranceTones)"/>
    </g>
    <path d="M0,85 C130,60 260,175 430,150" fill="none" stroke="var(--blue)" stroke-width="9"/>
    <path d="M0,352 C150,334 330,384 480,430" fill="none" stroke="var(--orange)" stroke-width="12"/>
    <circle cx="610" cy="195" r="264" fill="var(--yellow)"/>
    <circle cx="610" cy="195" r="256" fill="var(--orange)"/>
    <circle cx="610" cy="195" r="248" fill="var(--blue)"/>
    <g role="img" aria-label="Photo of the resort clubhouse and swimming pool">
      <circle cx="610" cy="195" r="241" fill="url(#poolTones)"/>
    </g>
  </svg>

  <h1 class="resort-title">Marlow Tide Resort</h1>
  <div class="sun-art" role="img" aria-label="Decorative sun illustration"></div>
  <p class="headline">JUST SOLD</p>

  <div class="agent-mark">
    <div class="agent-name">BRENDA KETTLE</div>
    <div class="agent-title">BROKER ASSOCIATE</div>
  </div>
  <div class="brokerage-mark">
    <span class="mark-square"></span>
    <span class="brokerage-name">R and P</span>
  </div>
</section>

<section class="card card-back">
  <svg class="shapes" width="690" height="536" viewBox="0 0 690 536">
    <defs>
      <linearGradient id="fadedWash" x1="0" y1="0" x2="0" y2="1">
        <stop offset="0" stop-color="#f3f4f3"/>
        <stop offset="1" stop-color="#dfe1df"/>
      </linearGradient>
      <linearGradient id="stripWash" x1="0" y1="0" x2="1" y2="0">
        <stop offset="0" stop-color="#f8e44a"/>
        <stop offset="1" stop-color="#f6dc2c"/>
      </linearGradient>
      <clipPath id="aboveStrip">
        <rect width="690" height="333"/>
      </clipPath>
      <linearGradient id="circleFade" x1="0" y1="0" x2="0" y2="1">
        <stop offset="0" stop-color="#e4e6e4"/>
        <stop offset=".7" stop-color="#eceeec"/>
        <stop offset="1" stop-color="#f7f3d8"/>
      </linearGradient>
    </defs>
    <g role="img" aria-label="Faded photo of palm trees and resort buildings">
      <rect width="690" height="536" fill="url(#fadedWash)"/>
    </g>
    <rect y="333" width="690" height="203" fill="url(#stripWash)"/>
    <g clip-path="url(#aboveStrip)">
      <circle cx="80" cy="148" r="336" fill="var(--yellow)"/>
      <circle cx="80" cy="148" r="327" fill="var(--orange)"/>
      <circle cx="80" cy="148" r="319" fill="var(--blue)"/>
    </g>
    <g role="img" aria-label="Faded photo of the resort pool and palms">
      <circle cx="80" cy="148" r="312" fill="url(#circleFade)"/>
    </g>
  </svg>

  <div class="brokerage-mark">
    <span class="mark-square"></span>
    <span class="brokerage-name">R and P</span>
  </div>
  <address class="return-address">
    <div class="name">Brenda Kettle</div>
    <div class="line">1482, Heron Bend Road,</div>
    <div class="line">Saltmere, FL 30517</div>
  </address>

  <div class="sale-note">
    <div class="rule"></div>
    <p>In Marlow Tide Resort has just</p>
    <p>sold at $<span class="blank" style="width:110px"></span>on<span class="blank" style="width:52px"></span></p>
  </div>
  <p class="call-to-action">Please Contact me if you are interested in buying or selling property in the area</p>

  <div class="stamp-box"></div>

  <div class="contact-strip">
    <div class="agent-mark">
      <div class="agent-name">BRENDA KETTLE</div>
      <div class="agent-title">BROKER ASSOCIATE</div>
    </div>
    <p class="contact-line">brendakettle@brendakettlehomes.example</p>
    <p class="contact-line">555-203-7746</p>
  </div>
</section>

</body>
</html>
```